Branding product image: TOMBEL (Golden Papaya) in Plastic Cup (Ready to Eat)

The product is sliced Fruit in Light syrup
Flavour: TOMBEL (Golden Papaya)
The temporary product name: TOMBEL
I want the product design to be something 'fun', 'natural', and 'colourful'
The design concept could be anything depends on your imagination, but it must be eye catchy and attractive.
Basically, I want you to be creative in designing the logo and the overall graphic design for the label.
The measurement is 20 cm (Length) x 6,5 cm (Height)
The target customers are young and health conscious audiences (10 years - 65 years old).
Create something different. Something extraordinary.
Brief summary about the fruit:
This fruit only grows in certain part of the world. It grows in mountain area that is in tropical climate. The fruit flesh has a yellowish-golden color. It has an extraordinary taste (unlike normal papaya) and it suits very well with any dishes from cold appetizer, white/ red meat, desserts, and cocktails.
I need a packaging design for Fruit Cup productThe product is sliced Fruit in Light syrup.There will be various flavours i.e. apple, lychee, peach, papaya, etc.However, you may design the product using one sample flavour (i.e. papaya) first, as the designs of other flavours could be adjusted afterwards.The temporary product name is: RICCANAI want the product design to be something 'fun', 'natural', and 'colourful'.The design concept could be anything depends on your imagination. Basically, I want you to be creative in designing the logo and the overall graphic design for the label. - Create something different. Something extraordinary -Additional:The measurement is 20cm (Length) x 5cm (Height).The target customers are young audiences (10 years - 35 years old).The product design must stand out in the supermarket shelf.It must be eye catchy and attractive.Thank you,Harold-PLEASE REFER TO DESIGN SAMPLE ATTACHED TO HAVE A BETTER UNDERSTANDING FOR THE PRODUCT CONCEPT- Added Wednesday, September 17, 2014
Project Deadline Extended Reason: Haven't found a good design. Added Friday, September 19, 2014
Project Deadline Extended Reason: Need more time for designers to finalize and perfect the design.Thank you,Harold Added Monday, September 29, 2014
Project Deadline Extended Reason: I haven't found a great design yet. Added Tuesday, February 24, 2015
Reason: Getting better designs now. Still Open to new ideas while refining the latest designs from some designers.
Please do your best in submitting other great designs!

```html
<!DOCTYPE html>
<html lang="en">
<head>
<meta charset="UTF-8">
<title>LUPEDOS Golden Papaya – Cup Label</title>
<link rel="stylesheet" href="https://fonts.googleapis.com/css2?family=Open+Sans:wght@700;800&display=swap">
<style>
  :root {
    --peach-edge: #fbc4a2;
    --peach-mid: #fde0b8;
    --cream: #fff4cf;
    --orange: #f27d12;
    --orange-deep: #e8670a;
    --brown: #6e3a22;
    --papaya-skin: #d9a53a;
    --papaya-flesh: #f08a2a;
    --papaya-seed: #5a3a22;
  }
  html, body {
    margin: 0;
    padding: 0;
    width: 1200px;
    height: 231px;
    overflow: hidden;
  }
  .label {
    position: relative;
    width: 1200px;
    height: 231px;
    overflow: hidden;
    background:
      radial-gradient(ellipse 520px 200px at 600px 110px, var(--cream) 0%, rgba(255,244,207,0) 100%),
      linear-gradient(90deg, var(--peach-edge) 0%, var(--peach-mid) 22%, var(--cream) 50%, var(--peach-mid) 78%, var(--peach-edge) 100%);
    font-family: "Open Sans", "Segoe UI", sans-serif;
  }
  .brand-name {
    position: absolute;
    left: 318px;
    top: 36px;
    margin: 0;
    font-weight: 700;
    font-size: 40px;
    letter-spacing: 1px;
    color: var(--brown);
    transform: rotate(-8deg);
    transform-origin: left center;
    line-height: 1;
  }
  .product-title {
    position: absolute;
    margin: 0;
    font-weight: 800;
    color: var(--orange);
    line-height: 1;
    text-shadow: 3px 3px 0 var(--brown);
    transform-origin: left center;
  }
  .product-title--first {
    left: 300px;
    top: 68px;
    font-size: 92px;
    letter-spacing: -1px;
    transform: rotate(-9deg);
  }
  .product-title--second {
    left: 412px;
    top: 124px;
    font-size: 70px;
    letter-spacing: -1px;
    transform: rotate(-9deg);
  }
  .serving-note {
    position: absolute;
    left: 520px;
    top: 186px;
    margin: 0;
    font-weight: 700;
    font-size: 21px;
    color: var(--orange-deep);
    text-shadow: 1px 1px 0 var(--brown);
    transform: rotate(-9deg);
    transform-origin: left center;
    line-height: 1;
  }
  .fruit-visual {
    position: absolute;
    left: 672px;
    top: 14px;
    width: 232px;
    height: 180px;
  }
</style>
</head>
<body>
  <main class="label">
    <p class="brand-name">LUPEDOS</p>
    <h1 class="product-title product-title--first">Golden</h1>
    <p class="product-title product-title--second">Papaya</p>
    <p class="serving-note">in LIGHT SYRUP</p>

    <svg class="fruit-visual" viewBox="0 0 232 180" role="img" aria-label="Illustration of a whole golden papaya beside a halved papaya showing orange flesh and dark seeds">
      <defs>
        <radialGradient id="fruitTone" cx="55%" cy="50%" r="60%">
          <stop offset="0%" stop-color="var(--papaya-flesh)"/>
          <stop offset="60%" stop-color="var(--papaya-skin)"/>
          <stop offset="100%" stop-color="var(--papaya-skin)" stop-opacity="0"/>
        </radialGradient>
      </defs>
      <rect x="0" y="0" width="232" height="180" rx="70" fill="url(#fruitTone)"/>
    </svg>
  </main>
</body>
</html>
```